Quellmar Aus Business card revamp

We are looking to revamp our business card design. We are hoping to change our colours to dark navey blue, gray, white and black but are open to keeping the same if a good design is submited. We are after somthing a bit differnt not just boring business card. I have attached a copy of our current card. We Want to keep the same logo design which i have attached a few to hopfully help you in this process. We are after a design that can be personalized to separate 4 people

Industry/Entity Type

Business

Colors
0455a3
ffffff
000000
cbcbcb

Requirements
Must have
• Quellmar Logo, address 3/41 Wattlebend Street, Kelvanby 4517, phone number, Name and position

```html
<!DOCTYPE html>
<html lang="en">
<head>
<meta charset="utf-8">
<title>Quellmar Aus – Business Card</title>
<link rel="stylesheet" href="https://fonts.googleapis.com/css2?family=Archivo:ital,wght@0,800;1,600;1,800&family=Roboto:wght@400;500;700&display=swap">
<style>
  :root {
    --brand-blue: #0a62b5;
    --brand-blue-dark: #0455a3;
    --accent-orange: #f07a1f;
    --paper: #ffffff;
    --ink-gray: #6d6d6d;
    --backdrop: #e7e8ea;
  }
  * { box-sizing: border-box; margin: 0; padding: 0; }
  html, body { width: 1200px; height: 800px; overflow: hidden; }
  body {
    background: var(--backdrop);
    position: relative;
    font-family: "Roboto", Arial, sans-serif;
  }

  .card {
    position: absolute;
    border-radius: 3px;
    box-shadow: 0 6px 18px rgba(0,0,0,0.12);
    overflow: hidden;
  }

  /* Front */
  .card-front {
    left: 70px; top: 230px;
    width: 580px; height: 350px;
    background: var(--brand-blue);
    color: var(--paper);
  }
  .front-logo {
    position: absolute;
    left: 0; right: 0; top: 112px;
    display: flex; flex-direction: column; align-items: center;
  }
  .logo-row { display: flex; align-items: center; gap: 14px; }
  .logo-dot {
    width: 34px; height: 34px; border-radius: 50%;
    background: var(--paper);
  }
  .logo-name {
    font-family: "Archivo", Arial, sans-serif;
    font-weight: 800;
    font-size: 58px;
    letter-spacing: -1px;
    line-height: 1;
  }
  .front-logo .logo-sub {
    font-family: "Archivo", Arial, sans-serif;
    font-weight: 800;
    font-size: 23px;
    margin-top: 6px;
    letter-spacing: 0.5px;
  }
  .front-footer {
    position: absolute;
    left: 0; right: 0; bottom: 48px;
    display: flex; align-items: center;
  }
  .accent-square {
    width: 16px; height: 22px;
    background: var(--accent-orange);
  }
  .tagline {
    font-family: "Archivo", Arial, sans-serif;
    font-style: italic;
    font-weight: 600;
    font-size: 16px;
    margin-left: 36px;
    white-space: nowrap;
  }
  .tagline strong { font-weight: 800; }
  .tagline-rule {
    flex: 1;
    height: 1px;
    background: rgba(255,255,255,0.85);
    margin-left: 14px;
  }

  /* Back */
  .card-back {
    left: 760px; top: 100px;
    width: 350px; height: 580px;
    background: var(--paper);
  }
  .back-logo {
    position: absolute;
    left: 0; right: 0; top: 110px;
    display: flex; flex-direction: column; align-items: center;
    color: var(--brand-blue);
  }
  .back-logo .logo-dot { width: 20px; height: 20px; background: var(--accent-orange); }
  .back-logo .logo-row { gap: 10px; }
  .back-logo .logo-name { font-size: 36px; letter-spacing: -0.5px; }
  .back-logo .logo-sub {
    font-family: "Archivo", Arial, sans-serif;
    font-weight: 800;
    font-size: 14px;
    margin-top: 4px;
  }
  .contact {
    position: absolute;
    left: 70px; bottom: 90px;
  }
  .person-name {
    color: var(--accent-orange);
    font-weight: 700;
    font-size: 20px;
  }
  .person-role {
    color: var(--ink-gray);
    font-size: 14px;
    margin-top: 2px;
  }
  .contact-rule {
    width: 34px; height: 2px;
    background: var(--accent-orange);
    margin: 28px 0 26px;
  }
  .contact-line {
    display: flex; align-items: flex-start; gap: 10px;
    color: var(--ink-gray);
    font-size: 14px;
    line-height: 1.45;
  }
  .contact-line + .contact-line { margin-top: 2px; }
  .contact-line svg { flex: none; margin-top: 3px; }
</style>
</head>
<body>

  <section class="card card-front" aria-label="Business card front">
    <div class="front-logo">
      <div class="logo-row">
        <span class="logo-dot"></span>
        <span class="logo-name">Quellmar</span>
      </div>
      <div class="logo-sub">Passive Fire Protection</div>
    </div>
    <div class="front-footer">
      <span class="accent-square"></span>
      <p class="tagline">Reliability with <strong>Dedication to Service</strong></p>
      <span class="tagline-rule"></span>
    </div>
  </section>

  <section class="card card-back" aria-label="Business card back">
    <div class="back-logo">
      <div class="logo-row">
        <span class="logo-dot"></span>
        <span class="logo-name">Quellmar</span>
      </div>
      <div class="logo-sub">Passive Fire Protection</div>
    </div>

    <div class="contact">
      <p class="person-name">Daniel Harrow</p>
      <p class="person-role">Managing Director</p>
      <div class="contact-rule"></div>
      <div class="contact-line">
        <svg width="12" height="12" viewBox="0 0 24 24" aria-hidden="true">
          <path fill="#f07a1f" d="M6.6 10.8a15.1 15.1 0 0 0 6.6 6.6l2.2-2.2c.3-.3.7-.4 1-.2 1.1.4 2.3.6 3.6.6.6 0 1 .4 1 1V20c0 .6-.4 1-1 1C10.6 21 3 13.4 3 4c0-.6.4-1 1-1h3.5c.6 0 1 .4 1 1 0 1.3.2 2.5.6 3.6.1.3 0 .7-.2 1z"/>
        </svg>
        <span>(+61) 07 3948 2615</span>
      </div>
      <div class="contact-line">
        <svg width="12" height="14" viewBox="0 0 24 28" aria-hidden="true">
          <path fill="#f07a1f" d="M12 0C6.5 0 2 4.5 2 10c0 7.5 10 18 10 18s10-10.5 10-18C22 4.5 17.5 0 12 0zm0 14a4 4 0 1 1 0-8 4 4 0 0 1 0 8z"/>
        </svg>
        <span>3/41 Wattlebend Street<br>Kelvanby 4517</span>
      </div>
    </div>
  </section>

</body>
</html>
```